Sign for our backyard barnyard

Want a sign to be printed/painted on a 2'x4' board for my wife's backyard barnyard.
Updates

Reason: This is the only extension I can offer to complete the project on time. Thank you for the submissions received so far.

Reason: We are so close to final selection!

Target Market(s)

Our friends who come to visit the barnyard! This is a birthday present for my wife who takes care of the animals.

Font styles to use
Other font styles liked:
• A font that gives the image of a rural farm setting.

Requirements
Must have
• Barnyard is called Willow Brook Patch. Should have a "farm style" letter treatment of that name as a logo element. Each of the 3 words should have a theme component, don't have to be obvious (like a big smile for happy) but should be worked subtly into design. Current animals in barnyard include chickens, goats and a potbelly pig so animal imagery or silhouette for those is good. Classic "Barn Red" is a good background or theme color for the design. Sign should be horizontally oriented. Needs to be printed on something that holds up outside but can be on plastic that mounts to wood.

```html
<!DOCTYPE html>
<html lang="en">
<head>
<meta charset="utf-8">
<title>Willow Brook Patch – Barnyard Sign</title>
<link href="https://fonts.googleapis.com/css2?family=Rye&display=swap" rel="stylesheet">
<style>
  :root {
    --barn-red: #b3000f;
    --barn-red-dark: #7d0009;
    --barn-red-light: #c8101c;
    --plank-seam: #4a0006;
    --metal-light: #f2f2f2;
    --metal-mid: #cfcfcf;
    --metal-dark: #a9a9a9;
    --sign-white: #f4f4f2;
    --silhouette: #e6e6e4;
  }
  html, body {
    margin: 0;
    padding: 0;
    width: 1200px;
    height: 600px;
    overflow: hidden;
    background: #ffffff;
  }
  .sign {
    position: relative;
    width: 1200px;
    height: 600px;
    background: linear-gradient(180deg, var(--metal-light), var(--metal-mid) 50%, var(--metal-dark));
  }
  .sign__board {
    position: absolute;
    left: 30px;
    top: 32px;
    width: 1140px;
    height: 536px;
    background:
      repeating-linear-gradient(180deg,
        transparent 0 116px,
        var(--plank-seam) 116px 120px),
      radial-gradient(ellipse at 50% 40%, var(--barn-red-light), var(--barn-red) 55%, var(--barn-red-dark));
    background-position: 0 23px, 0 0;
    box-shadow: inset 0 0 40px rgba(0,0,0,0.45);
  }
  .sign__art {
    position: absolute;
    inset: 0;
  }
  .sign__title {
    font-family: "Rye", "Georgia", serif;
    fill: var(--sign-white);
  }
  .sign__animal {
    fill: var(--silhouette);
  }
</style>
</head>
<body>
  <div class="sign">
    <div class="sign__board"></div>
    <svg class="sign__art" width="1200" height="600" viewBox="0 0 1200 600" xmlns="http://www.w3.org/2000/svg">
      <defs>
        <path id="line-one" d="M 300 200 Q 585 160 870 200"/>
        <path id="line-two" d="M 120 435 Q 600 245 1080 435"/>
        <filter id="title-shadow" x="-10%" y="-20%" width="120%" height="140%">
          <feDropShadow dx="4" dy="5" stdDeviation="3" flood-color="#280000" flood-opacity="0.8"/>
        </filter>
      </defs>

      <text class="sign__title" filter="url(#title-shadow)" text-anchor="middle">
        <textPath href="#line-one" startOffset="50%"><tspan font-size="150">W</tspan><tspan font-size="108">ILLOW</tspan></textPath>
      </text>
      <text class="sign__title" filter="url(#title-shadow)" text-anchor="middle">
        <textPath href="#line-two" startOffset="50%"><tspan font-size="146">B</tspan><tspan font-size="100">ROOK </tspan><tspan font-size="146">P</tspan><tspan font-size="100">ATCH</tspan></textPath>
      </text>

      <g class="sign__animals">
        <rect class="sign__animal" x="295" y="465" width="160" height="85" rx="30"
              role="img" aria-label="White silhouette of a potbelly pig"/>
        <rect class="sign__animal" x="505" y="420" width="230" height="140" rx="24"
              role="img" aria-label="White silhouette of a goat"/>
        <rect class="sign__animal" x="745" y="460" width="75" height="85" rx="20"
              role="img" aria-label="White silhouette of a chicken"/>
      </g>
    </svg>
  </div>
</body>
</html>
```